New Cryotherapy Business needs a Flyer Design

We are expanding our massage business located in Sydney with a Cryosauna. We need a flyer/brochure that explain what whole body cryotherapy is and all its benefits in a very simple way as we are the first cryotherapy business in Sydney and not many people knows what it is yet. We would like to see a design that use the color of our logo or shades of blue that comunicate freshness, innovation and health but also movement and sport performance. The flyer targets gym's members, athletes and also yoga/pilates goers with a focus on wellbeing and health.

Please find attached our logo (we actually prefer to use the logo/font in the banner adding the hand underneath the vitruvian man) and some examples of cryotherapy flyers with the information about the product/service we would like to include in the flyer. We would like also to include a section with special offer for new clients.

Target Market(s)

The flyer targets gym's members, athletes and also yoga/pilates goers with a focus on wellbeing and health.

Industry/Entity Type

Health And Wellness

Font styles to use
Sans Serif

Colors
f78f20
848484
c3c3c3
85acd3
0792cd
3176b5

Requirements
Must have
• logo, contact details, FAQs, About WBC, Benefits, Applications include, special offer for new clients section, pic of cryosauna with muscular guy, logos of "as seen on tv"

```html
<!DOCTYPE html>
<html lang="en">
<head>
<meta charset="utf-8">
<title>Kelva Whole Body Cryotherapy Brochure</title>
<link href="https://fonts.googleapis.com/css2?family=Archivo+Black&family=Open+Sans:wght@400;600;700&family=Roboto+Condensed:wght@400;700&display=swap" rel="stylesheet">
<style>
:root{
  --ink:#000;
  --panel:#0b0b0d;
  --white:#fff;
  --cyan:#1ab0f0;
  --blue:#0792cd;
  --blue-deep:#3176b5;
  --blue-soft:#85acd3;
  --grey:#848484;
  --grey-light:#c3c3c3;
  --orange:#f78f20;
  --alert:#e8432b;
  --page:#ededed;
}
*{margin:0;padding:0;box-sizing:border-box}
html,body{width:1200px;height:2601px;overflow:hidden;background:var(--page)}
body{position:relative;font-family:"Roboto Condensed",Arial,sans-serif;color:var(--white)}
.spread{position:absolute;left:0;width:1200px;height:901px;background:var(--ink);overflow:hidden}
.spread-outside{top:0}
.spread-inside{top:902px}
.abs{position:absolute}
.photo{position:absolute}
.band{position:absolute;left:455px;width:290px;background:linear-gradient(180deg,var(--blue) 0%,var(--blue-deep) 100%)}
.band-wave{position:absolute;left:400px;width:400px}
.faq{left:40px;top:380px;width:340px;font-weight:700;font-size:12.5px;line-height:1.32;text-transform:uppercase}
.faq h3{color:var(--cyan);font-size:16px;margin:0 0 4px}
.faq p{margin-bottom:16px}
.tv-title{left:455px;top:292px;width:290px;text-align:center;font-family:"Open Sans",sans-serif;font-style:italic;font-weight:700;font-size:16px}
.tv-board{left:508px;top:315px;width:185px;height:290px;background:var(--white);display:grid;grid-template-columns:repeat(3,1fr);gap:14px 10px;padding:14px 12px}
.tv-board span{background:var(--grey-light);border-radius:2px}
.contact{left:490px;width:260px;font-family:"Open Sans",sans-serif;font-size:14px;font-weight:600;line-height:1.25}
.contact-phone{font-size:22px;font-weight:400}
.icon{position:absolute;left:424px}
.offer{left:590px;top:795px;width:148px;height:98px;background:var(--white);padding:3px}
.offer-inner{border:2px solid var(--blue);height:100%;text-align:center;color:var(--blue);font-family:"Open Sans",sans-serif;padding-top:4px}
.offer-title{font-weight:700;font-size:13px;line-height:1.05}
.offer-sub{font-size:9px;font-weight:600;line-height:1}
.offer-price{font-size:30px;font-weight:700;line-height:1.1}
.offer-price small{font-size:10px;font-weight:400}
.offer-note{font-size:7px;color:var(--grey)}
.brand{text-align:center;color:var(--white)}
.brand-mark{width:22px;height:22px;border:1.5px solid var(--white);border-radius:50%;margin:0 auto 4px}
.brand-name{font-family:"Open Sans",sans-serif;font-weight:400;letter-spacing:4px}
.brand-tag{font-family:"Open Sans",sans-serif;font-size:7px;letter-spacing:.5px}
.hero-title{left:848px;top:295px;width:300px;font-family:"Archivo Black",sans-serif;font-size:72px;line-height:.9;color:var(--grey-light);text-shadow:3px 3px 0 #333}
.hero-bar{left:818px;top:455px;width:380px;height:62px;background:linear-gradient(180deg,#f2f2f2,var(--grey-light));font-family:"Archivo Black",sans-serif;font-size:44px;line-height:62px;color:#222;padding-left:8px}
.hero-bar .cyan{color:var(--cyan)}
.just{left:955px;top:545px;width:100px;text-align:center;font-weight:700;font-size:15px;line-height:1.2}
.just b{display:block;font-size:56px;color:var(--cyan);line-height:1}
.book{left:820px;top:745px;width:380px;height:65px;border:2px solid var(--white);border-right:none;padding:6px 0 0 36px}
.book-title{font-family:"Open Sans",sans-serif;font-size:17px;letter-spacing:.5px}
.book-url{font-family:"Open Sans",sans-serif;font-weight:700;font-size:19px}
.globe{position:absolute;left:8px;top:33px}
.squares span{position:absolute;background:var(--cyan)}
.inside-title{left:0;top:1105px;width:400px;text-align:center}
.inside-title .big{font-family:"Archivo Black",sans-serif;font-size:40px;line-height:.95}
.inside-title .small{font-family:"Open Sans",sans-serif;font-size:24px;line-height:1.1}
.inside-title .small em{font-style:normal;color:var(--cyan)}
.about-head{left:115px;top:1218px;color:var(--alert);font-family:"Archivo Black",sans-serif;font-size:22px}
.about{left:28px;top:1245px;width:360px;font-weight:700;font-size:13px;line-height:1.38;text-transform:uppercase}
.about em{font-style:normal;color:var(--cyan)}
.how-head{left:70px;top:1590px;font-family:"Archivo Black",sans-serif;font-size:24px;display:flex;align-items:center;gap:8px}
.how-box{left:0;top:1630px;width:400px;height:115px;background:var(--blue);border:2px solid var(--white);padding:8px 12px;font-weight:700;font-size:12.5px;line-height:1.3;text-transform:uppercase}
.apps-head{left:445px;top:1238px;width:310px;text-align:center;font-family:"Open Sans",sans-serif;font-weight:700;font-size:31px;letter-spacing:1px;border-top:2px solid var(--white);border-bottom:2px solid var(--white);line-height:40px}
.apps{left:455px;top:1290px;width:290px;list-style:none;text-align:center;font-family:"Open Sans",sans-serif;font-weight:700;font-style:italic;font-size:12.5px;line-height:1}
.apps li{height:27.5px;display:flex;justify-content:center;align-items:center;gap:6px;white-space:nowrap}
.apps small{font-size:9px}
.tick{width:11px;height:11px;flex:none}
.athletes{left:520px;top:1672px;width:145px;height:88px;background:var(--white);border:2px solid var(--blue);text-align:center;color:var(--blue);font-family:"Open Sans",sans-serif;font-weight:700;font-size:9px;padding-top:6px}
.athletes-row{display:flex;justify-content:center;gap:5px;margin-top:8px}
.athletes-row span{width:26px;height:32px;background:var(--grey-light);border-radius:3px}
.benefits-head{left:935px;top:1615px;width:125px;height:34px;background:var(--white);color:var(--blue);font-family:"Archivo Black",sans-serif;font-size:26px;line-height:34px;text-align:center}
.benefits{top:1668px;list-style:none;font-weight:700;font-size:11.5px;line-height:1.18;text-transform:uppercase}
.benefits li{display:flex;align-items:center;gap:5px;white-space:nowrap}
.benefits small{font-size:7px}
</style>
</head>
<body>
<svg width="0" height="0" style="position:absolute">
  <defs>
    <symbol id="tick" viewBox="0 0 12 12"><path d="M1 6.5 L4.5 10 L11 2" fill="none" stroke="#fff" stroke-width="2.4"/></symbol>
  </defs>
</svg>

<!-- Outside spread -->
<section class="spread spread-outside">
  <div class="photo" style="left:0;top:0;width:400px;height:345px;background:radial-gradient(ellipse at 40% 40%,#d8dde2 0%,#7d858c 40%,#101214 85%)" role="img" aria-label="Close-up of ice cubes on a dark background"></div>
  <div class="photo" style="left:400px;top:0;width:400px;height:330px;background:radial-gradient(ellipse at 50% 45%,#9fb2c4 0%,#4c6070 40%,#0c1218 85%)" role="img" aria-label="Woman seen from behind holding her shoulders inside the cryosauna"></div>
  <div class="photo" style="left:800px;top:0;width:400px;height:901px;background:linear-gradient(180deg,#161616 0%,#2a2a2c 35%,#1b1b1d 70%,#0a0a0a 100%)" role="img" aria-label="Cryosauna chamber in dark studio lighting"></div>

  <div class="faq abs">
    <h3>How do I feel after treatment?</h3>
    <p>Your external skin temperature warms up within five minutes of exiting the cryosauna. The immediate effects from each session typically last for six to eight hours. Cryotherapy stimulates the body to release endorphins, which are the hormones that make you feel good and energetic. Most clients report a better night's sleep after just one session!</p>
    <h3>Is it safe?</h3>
    <p>Yes. It has shown to be both safe and effective for a staggering variety of conditions and goals. Nitrogen is a non-toxic gas that makes up about 78% of the air we breathe. However, breathing pure nitrogen could cause fainting, due to the lack of oxygen. To prevent this, the cryosauna is designed to keep the patient's head above the chamber, and patients are instructed to breathe up room-air.</p>
    <h3>Is it comfortable?</h3>
    <p>Where an ice bath has direct contact with the skin and can be painful, cryotherapy is a dry, indirect contact. Due to the session only being three minutes max, the session is very tolerable. Towards the end of the session, you may get a 'pins and needles' sensation, which disappears immedi-</p>
  </div>

  <svg class="band-wave" style="top:235px" width="400" height="70" viewBox="0 0 400 70">
    <path d="M0 55 C120 10 260 0 400 40 L400 70 L0 70Z" fill="#1c1c1c"/>
    <path d="M55 45 C150 15 250 12 345 30 L345 70 L55 70Z" fill="#0792cd"/>
    <path d="M0 50 C130 5 270 -2 400 35" fill="none" stroke="#85acd3" stroke-width="3"/>
  </svg>
  <div class="band" style="top:290px;height:611px"></div>

  <div class="tv-title abs">AS SEEN ON TV</div>
  <div class="tv-board abs" aria-label="Television features">
    <span></span><span></span><span></span><span></span><span></span><span></span><span></span><span></span><span></span><span></span><span></span><span></span><span></span><span></span><span></span>
  </div>

  <svg class="icon" style="top:652px" width="22" height="30" viewBox="0 0 22 30"><path d="M11 1C5 1 1 5.5 1 11c0 7 10 18 10 18s10-11 10-18C21 5.5 17 1 11 1z" fill="#1ab0f0"/><circle cx="11" cy="11" r="4" fill="#000"/></svg>
  <div class="contact abs" style="top:645px">SUITE 4, 18 HARBOUR LANE<br>EASTWOOD BAY NSW<br>2000 AU</div>
  <svg class="icon" style="top:717px" width="22" height="24" viewBox="0 0 22 24"><rect x="1" y="1" width="20" height="22" rx="3" fill="none" stroke="#fff" stroke-width="2"/><path d="M7 6c0 6 3 10 8 12l2-2-3-2-1 1c-2-1-3-3-4-5l1-1-1-3z" fill="#fff"/></svg>
  <div class="contact contact-phone abs" style="top:715px">(0) 400-123-456</div>
  <svg class="icon" style="top:765px" width="24" height="18" viewBox="0 0 24 18"><rect x="1" y="1" width="22" height="16" fill="none" stroke="#fff" stroke-width="1.8"/><path d="M1 1l11 9 11-9" fill="none" stroke="#fff" stroke-width="1.8"/></svg>
  <div class="contact abs" style="top:765px;font-size:15px">INFO@KELVACRYO.COM.AU</div>

  <div class="offer abs">
    <div class="offer-inner">
      <div class="offer-title">SPECIAL OFFER</div>
      <div class="offer-sub">INTRODUCTORY SESSION</div>
      <div class="offer-price">$75 <small>Regular Price $90</small></div>
      <div class="offer-note">(for new WBC clients only)</div>
    </div>
  </div>

  <div class="brand abs" style="left:960px;top:60px;width:180px">
    <div class="brand-mark"></div>
    <div class="brand-name" style="font-size:40px;line-height:1">KELVA</div>
    <div class="brand-tag">KELVA WELLNESS STUDIO</div>
  </div>

  <div class="hero-title abs">WHOLE<br>BODY</div>
  <div class="hero-bar abs"><span class="cyan">CYRO</span>THERAPY</div>
  <div class="just abs">JUST<b>3</b>MINUTES<br>FOR<br>WHOLE<br>BODY<br>RECOVERY</div>
  <div class="book abs">
    <svg class="globe" width="22" height="22" viewBox="0 0 22 22"><circle cx="11" cy="11" r="9.5" fill="none" stroke="#fff" stroke-width="1.6"/><ellipse cx="11" cy="11" rx="4" ry="9.5" fill="none" stroke="#fff" stroke-width="1.4"/><path d="M1.5 11h19M3 6h16M3 16h16" stroke="#fff" stroke-width="1.2"/></svg>
    <div class="book-title">BOOK YOUR APPOINTMENT TODAY</div>
    <div class="book-url">WWW.KELVACRYO.COM</div>
  </div>
</section>

<!-- Inside spread -->
<section class="spread spread-inside">
  <div class="squares">
    <span style="left:112px;top:22px;width:24px;height:24px"></span>
    <span style="left:142px;top:52px;width:14px;height:14px"></span>
    <span style="left:100px;top:58px;width:18px;height:18px"></span>
    <span style="left:160px;top:78px;width:20px;height:20px"></span>
    <span style="left:185px;top:55px;width:10px;height:10px"></span>
    <span style="left:125px;top:88px;width:12px;height:12px"></span>
  </div>
  <div class="photo" style="left:0;top:110px;width:400px;height:170px;background:radial-gradient(ellipse at 50% 45%,#8a98a6 0%,#3a4550 40%,#060708 80%)" role="img" aria-label="Swimmer doing butterfly stroke with water splashing"></div>
  <div class="photo" style="left:400px;top:0;width:400px;height:240px;background:radial-gradient(ellipse at 50% 50%,#f4f4f4 0%,#a9a9a9 45%,#222 90%)" role="img" aria-label="Quilted silver interior of the cryosauna chamber"></div>
  <div class="photo" style="left:800px;top:0;width:400px;height:720px;background:radial-gradient(ellipse at 55% 55%,#b9c3cc 0%,#5d6670 30%,#1e2024 60%,#000 90%)" role="img" aria-label="Muscular man stepping out of an open cryosauna surrounded by vapour"></div>

  <div class="inside-title abs" style="top:205px">
    <div class="big">WHOLE<br>BODY</div>
    <div class="small">CRY<em>O</em>THERAPY</div>
  </div>
  <div class="about-head abs" style="top:316px">ABOUT:</div>
  <div class="about abs" style="top:345px">WBC (<em>Whole Body Cryotherapy</em>) was first utilized in Japan in the early 1970's by Dr. Hoshino to treat rheumatoid arthritis and inflammatory join diseases. Proving extremely effective, WBC quickly gained notoriety for that specific issue, but also to treat systemic inflammation processes throughout the body. Now elite athletes and pro teams have adopted WBC for muscle and injury recovery and as a powerful treatment to decrease recovery time and increase athletic performance and boost the body's metabolic rate. WBC is becoming worldwide well documented as being used for the daily management of pain, inflammation, energy, and stress related conditions. KelvaCryo is one of the first few centres opened in Sydney aiming for the most safe, effective, and affordable treatments available to the public.</div>
  <div class="how-head abs" style="top:690px"><svg width="22" height="22" viewBox="0 0 12 12"><use href="#tick"/></svg>HOW IT WORKS:</div>
  <div class="how-box abs" style="top:728px">With whole body cryotherapy (WBC) the body is exposed to ultra-low temperatures (-200 to -240F). The client is placed in a cryogenic sauna/chamber for a short duration of 1.5-3 minutes which lowers the client's skin surface temperature significantly and stimulates receptors.</div>

  <svg class="band-wave" style="top:150px" width="400" height="60" viewBox="0 0 400 60">
    <path d="M55 40 C150 5 260 0 345 20 L345 60 L55 60Z" fill="#0792cd"/>
    <path d="M0 45 C140 0 280 -5 400 28" fill="none" stroke="#85acd3" stroke-width="3"/>
  </svg>
  <div class="band" style="top:190px;height:711px"></div>

  <div class="apps-head abs" style="top:335px">APPLICATIONS</div>
  <ul class="apps abs" style="top:388px">
    <li><svg class="tick"><use href="#tick"/></svg>ATHLETIC PERFORMANCE</li>
    <li><svg class="tick"><use href="#tick"/></svg>ATHLETIC RECOVERY</li>
    <li><svg class="tick"><use href="#tick"/></svg>POSTSURGICAL RECOVERY</li>
    <li><svg class="tick"><use href="#tick"/></svg>MUSCULOSKELETAL INJURIES</li>
    <li><svg class="tick"><use href="#tick"/></svg>OSTEOARTHRITIS - RHEUMATOID ARTHRITIS</li>
    <li><svg class="tick"><use href="#tick"/></svg>OSTEOARTHRITIS - MULTIPLE SCLEROSIS</li>
    <li><svg class="tick"><use href="#tick"/></svg>FIBROMYALGIA <small>- CHRONIC FATIGUE SYNDROME</small></li>
    <li><svg class="tick"><use href="#tick"/></svg>DEPRESSION &amp; MOOD DISORDERS</li>
    <li><svg class="tick"><use href="#tick"/></svg>WEIGHT MANAGEMENT</li>
    <li><svg class="tick"><use href="#tick"/></svg>DEGENERATIVE DISEASES OF JOINTS &amp; SPINE</li>
    <li><svg class="tick"><use href="#tick"/></svg>PHANTOM PAIN - CHRONIC PAIN SYNDROME</li>
    <li><svg class="tick"><use href="#tick"/></svg>AUTOIMMUNE <small>AND OTHER INFLAMMATORY DISORDERS</small></li>
    <li><svg class="tick"><use href="#tick"/></svg>SKIN DISORDERS <small>SUCH AS DERMATITIS AND PSORIASIS</small></li>
  </ul>
  <div class="athletes abs" style="top:770px">
    SERVING PRO ATHLETES<br>SINCE 2009
    <div class="athletes-row"><span></span><span></span><span></span><span></span></div>
  </div>

  <div class="brand abs" style="left:1070px;top:45px;width:120px">
    <div class="brand-mark" style="width:14px;height:14px"></div>
    <div class="brand-name" style="font-size:24px;line-height:1;letter-spacing:3px">KELVA</div>
    <div class="brand-tag" style="font-size:5px">KELVA WELLNESS STUDIO</div>
  </div>

  <div class="benefits-head abs" style="top:713px">BENIFITS</div>
  <ul class="benefits abs" style="left:832px;top:766px">
    <li><svg class="tick"><use href="#tick"/></svg>Pain management</li>
    <li><svg class="tick"><use href="#tick"/></svg>Rapid muscle recovery</li>
    <li><svg class="tick"><use href="#tick"/></svg>Injury therapy</li>
    <li><svg class="tick"><use href="#tick"/></svg>Performance enhancement</li>
    <li><svg class="tick"><use href="#tick"/></svg>Increased energy levels</li>
    <li><svg class="tick"><use href="#tick"/></svg>Increased libido</li>
    <li><svg class="tick"><use href="#tick"/></svg>Sleep better</li>
    <li><svg class="tick"><use href="#tick"/></svg>Better mood</li>
  </ul>
  <ul class="benefits abs" style="left:1008px;top:766px">
    <li><svg class="tick"><use href="#tick"/></svg>Metabolic &amp; immunity boost</li>
    <li><svg class="tick"><use href="#tick"/></svg>Caloric burn <small>- burn up to 800 calories</small></li>
    <li><svg class="tick"><use href="#tick"/></svg>Anti-aging</li>
    <li><svg class="tick"><use href="#tick"/></svg>Skin rejuvenation</li>
    <li><svg class="tick"><use href="#tick"/></svg>Improved skin elasticity</li>
    <li><svg class="tick"><use href="#tick"/></svg>Increased collagen production</li>
    <li><svg class="tick"><use href="#tick"/></svg>Cellulite reduction</li>
  </ul>
</section>
</body>
</html>
```